Shopguidance.net

I've attached two different logo's which I both like and would like to see different designs with each logo. I'm starting a retail consulting business and blog. You can view the start of my project at shopguidance.net to get an idea of what I'm creating.
Looking for a design that says creative, strategic and community.
Updates
Hello Everyone,
Thank you for the amazing design so far.
What I Like
- double sided designs, front and back
- one side should be white or green. Customers cannot write on or make notes on an all black card
- Simple, cool, creative is best
My business card will only have the following
- Instagram
- Facebook
- Email
- Website
My new Tag line is
Think Smart. Lead Smart. Work Smart.
My title will be:
Tobin Marlowe
Retail Consultant
Please submit 1 or 2 designs with these specifications.
Thank you,
Tobin Marlowe
Reason: Looking for a few more designs and have now committed the project and it is no longer refundable. Please read brief and follow specific instructions.
Looking for something simple yet creative. Something that may stand out from most cards.
Thank you,
Tobin Marlowe
Thank you,
Tobin Marlowe
Target Market(s)
My main target is retail managers and retail businesses that are focused on leadership and people development.
Industry/Entity Type
Retail
Look and feel
Each slider illustrates characteristics of the customer's brand and the style your logo design should communicate.

```html
<!DOCTYPE html>
<html lang="en">
<head>
<meta charset="utf-8">
<title>Shopguidance – Business Card</title>
<link href="https://fonts.googleapis.com/css2?family=Questrial&family=Arimo:wght@400&display=swap" rel="stylesheet">
<style>
  :root {
    --backdrop: #e9e8e6;
    --card-top: #626264;
    --card-bottom: #4e4e50;
    --card-light: #ffffff;
    --brand-green: #5cbf2a;
    --text-light: #f4f4f4;
    --text-muted: #dcdcdc;
    --text-dark: #4a4a4c;
    --text-dark-muted: #6d6d70;
  }
  * { box-sizing: border-box; margin: 0; padding: 0; }
  html, body { width: 1200px; height: 918px; overflow: hidden; }
  body {
    background: var(--backdrop);
    display: flex;
    align-items: center;
    justify-content: center;
    gap: 60px;
    font-family: "Arimo", Arial, sans-serif;
  }
  .card {
    width: 520px;
    height: 298px;
    border-radius: 4px;
    box-shadow: 0 10px 28px rgba(0,0,0,.22);
    position: relative;
  }
  .brand-dot {
    border-radius: 50%;
    background: linear-gradient(180deg, #1fae3c, #8fd43a);
  }

  /* Front – dark */
  .card-front {
    background: radial-gradient(ellipse at 45% 40%, var(--card-top), var(--card-bottom));
    color: var(--text-light);
  }
  .card-front .brand-dot {
    position: absolute;
    left: 46px; top: 58px;
    width: 62px; height: 62px;
  }
  .card-front .brand-name {
    position: absolute;
    left: 46px; top: 132px;
    font-family: "Questrial", Arial, sans-serif;
    font-size: 56px;
    line-height: 64px;
    letter-spacing: -0.5px;
    color: var(--text-light);
  }
  .card-front .brand-web {
    position: absolute;
    left: 50px; top: 200px;
    font-size: 13px;
    color: var(--text-muted);
  }
  .card-front .tagline {
    position: absolute;
    left: 50px; top: 240px;
    font-family: "Questrial", Arial, sans-serif;
    font-size: 15px;
    letter-spacing: 0.3px;
    color: var(--brand-green);
  }

  /* Back – white, writable */
  .card-back {
    background: var(--card-light);
    color: var(--text-dark);
  }
  .card-back .brand-dot {
    position: absolute;
    left: 40px; top: 101px;
    width: 96px; height: 96px;
  }
  .card-back .details {
    position: absolute;
    left: 200px; top: 44px;
  }
  .card-back .brand-name {
    font-family: "Questrial", Arial, sans-serif;
    font-size: 24px;
    line-height: 30px;
    color: var(--brand-green);
  }
  .card-back .person-name {
    margin-top: 8px;
    font-family: "Questrial", Arial, sans-serif;
    font-size: 18px;
    line-height: 22px;
    color: var(--text-dark);
  }
  .card-back .person-title {
    font-size: 13px;
    line-height: 18px;
    color: var(--text-dark-muted);
    margin-bottom: 14px;
  }
  .contact-list { list-style: none; }
  .contact-list li {
    display: flex;
    align-items: center;
    gap: 12px;
    font-size: 15px;
    line-height: 26px;
    color: var(--text-dark);
  }
  .contact-list .label {
    width: 78px;
    font-size: 12px;
    color: var(--text-dark-muted);
    text-transform: uppercase;
    letter-spacing: 0.6px;
  }
  .contact-list svg { width: 14px; height: 14px; fill: var(--brand-green); flex: none; }
</style>
</head>
<body>

<section class="card card-front">
  <div class="brand-dot"></div>
  <div class="brand-name">Shopguidance</div>
  <div class="brand-web">www.shopguidance.net</div>
  <div class="tagline">Think Smart. Lead Smart. Work Smart.</div>
</section>

<section class="card card-back">
  <div class="brand-dot"></div>
  <div class="details">
    <div class="brand-name">Shopguidance</div>
    <div class="person-name">Tobin Marlowe</div>
    <div class="person-title">Retail Consultant</div>
    <ul class="contact-list">
      <li>
        <svg viewBox="0 0 14 14" aria-hidden="true"><rect x="2" y="2" width="10" height="10" rx="2"/></svg>
        <span class="label">Instagram</span>@shopguidance
      </li>
      <li>
        <svg viewBox="0 0 14 14" aria-hidden="true"><rect x="2" y="2" width="10" height="10" rx="2"/></svg>
        <span class="label">Facebook</span>/shopguidance
      </li>
      <li>
        <svg viewBox="0 0 14 14" aria-hidden="true"><path d="M1 3h12v8H1z"/></svg>
        <span class="label">Email</span>tobin@shopguidance.net
      </li>
      <li>
        <svg viewBox="0 0 14 14" aria-hidden="true"><path d="M7 1L1 6.5h1.8V13h3.4V9.5h1.6V13h3.4V6.5H13z"/></svg>
        <span class="label">Website</span>www.shopguidance.net
      </li>
    </ul>
  </div>
</section>

</body>
</html>
```